Stylish Business Card for Modern hair salon

I need a simple business card design using our salon logo and colours that are in the logo. We service clients of all ages but predominantly those in the 18 to 55 age range. We have a young staff and are looking to have a card that will present a modern and clean image that represents who we are. The card should be in black and white same as our logo. Minimal use of other colours is allowed.

Industry/Entity Type

Hair And Beauty

Contact Information for Business Card

The design should have the following information
salon name - TR Hair Studio
address - 2751 Birchfield Rd.E. Mississauga, ON L7P3K2
phone - 905 614-2870
website - trhairexample.ca
instagram - tr.hairstudio
twitter - @TR_HairStudio

Colors
000000
ffffff
474747

Requirements
Must have
• simple design, salon name, address, phone, website, instagram, twitter info
• Back of card should have the following:
• YOUR NEXT APPOINTMENT
• DATE
• TIME
Nice to have
• simple design, clear to see and read,
• predominantly black and white colour, minimal use of other colours is ok
Should not have
• many colours, various fonts

```html
<!DOCTYPE html>
<html lang="en">
<head>
<meta charset="utf-8">
<title>TR Hair Studio – Business Card</title>
<link href="https://fonts.googleapis.com/css2?family=Karla:wght@500;600;700&display=swap" rel="stylesheet">
<style>
  :root {
    --ink: #000000;
    --paper: #ffffff;
    --grey: #474747;
    --backdrop: #f2f2f2;
    --edge: #e0e0e0;
  }
  * { margin: 0; padding: 0; box-sizing: border-box; }
  html, body {
    width: 1200px; height: 762px; overflow: hidden;
    background: var(--backdrop);
    font-family: "Karla", Arial, sans-serif;
  }
  .canvas { position: relative; width: 1200px; height: 762px; }

  /* Front */
  .card-front {
    position: absolute; left: 70px; top: 212px;
    width: 582px; height: 333px;
    background: var(--ink); color: var(--paper);
  }
  .front-wordmark {
    position: absolute; left: 102px; top: 164px;
    transform: translate(-50%, -50%) rotate(-90deg);
    white-space: nowrap;
    font-size: 44px; font-weight: 600; letter-spacing: 6px;
    color: var(--paper);
  }
  .front-divider {
    position: absolute; left: 197px; top: 0;
    width: 2px; height: 100%; background: var(--paper);
  }
  .contact {
    position: absolute; left: 256px; top: 0;
    font-weight: 600; letter-spacing: 1px; font-size: 15.5px;
  }
  .contact p { position: absolute; left: 0; white-space: nowrap; line-height: 20px; }
  .studio-name { top: 67px; }
  .address { top: 108px; }
  .phone { top: 171px; }
  .website { top: 211px; letter-spacing: 0.6px; }
  .socials {
    position: absolute; left: 256px; top: 278px;
    display: flex; gap: 26px; font-size: 12.5px; font-weight: 600; letter-spacing: 0.6px;
  }
  .social { display: flex; align-items: center; gap: 10px; }
  .social-dot {
    width: 14px; height: 14px; border-radius: 50%;
    border: 2px solid var(--paper);
  }

  /* Back */
  .card-back {
    position: absolute; left: 754px; top: 85px;
    width: 332px; height: 592px;
    background: var(--paper); border: 1px solid var(--edge);
  }
  .back-wordmark {
    position: absolute; left: 0; top: 150px; width: 100%;
    text-align: center;
    font-size: 46px; font-weight: 600; letter-spacing: 6px;
    color: var(--ink);
  }
  .appointment-title {
    position: absolute; left: 0; top: 240px; width: 100%;
    text-align: center; font-size: 14px; font-weight: 600; letter-spacing: 1px;
    color: var(--grey);
  }
  .rule {
    position: absolute; left: 22px; width: 290px; background: var(--ink);
  }
  .rule-title { top: 273px; height: 2px; background: var(--grey); }
  .rule-date { top: 374px; height: 1px; }
  .rule-time { top: 472px; height: 1px; }
  .field-label {
    position: absolute; left: 23px; font-size: 14px; font-weight: 600; letter-spacing: 0.8px;
    color: var(--ink);
  }
  .label-date { top: 322px; }
  .label-time { top: 421px; left: 21px; }
</style>
</head>
<body>
<main class="canvas">
  <section class="card-front">
    <div class="front-wordmark">TR HAIR</div>
    <div class="front-divider"></div>
    <div class="contact">
      <p class="studio-name">TR HAIR STUDIO</p>
      <p class="address">2751 BIRCHFIELD RD E,<br>MISSISSAUGA, ON L7P 3K2</p>
      <p class="phone">905 614 2870</p>
      <p class="website">www.trhairexample.ca</p>
    </div>
    <div class="socials">
      <span class="social"><span class="social-dot"></span>tr.hairstudio</span>
      <span class="social"><span class="social-dot"></span>TR_HairStudio</span>
    </div>
  </section>

  <section class="card-back">
    <div class="back-wordmark">TR HAIR</div>
    <p class="appointment-title">YOUR NEXT APPOINTMENT</p>
    <div class="rule rule-title"></div>
    <p class="field-label label-date">DATE</p>
    <div class="rule rule-date"></div>
    <p class="field-label label-time">TIME</p>
    <div class="rule rule-time"></div>
  </section>
</main>
</body>
</html>
```